Tolvern Business Cards

Business card design. dont mind if new logo is suggested.
it would be for a security company.
our clients would be bigger security companies around Australia.
have a logo done but can be replaced. see attaached. like the colors.
Need company name, person name, designation, phone and email on front.
At back company logo and name. website saddress and 2 x license numbers
would like to have 2 different background color for both sidde

Industry/Entity Type

Security

Contact Information for Business Card

round corners, front should be light in color. need logo at back with webaddress and 2 x license numners

Font styles to use
Sans Serif

Colors
f37122
faa54b
f8ba93
0255a3
0592cd
85cae6
b3d448
9bcb3c
ffffff

Requirements
Must have
• see description
Nice to have
• see description
Should not have
• should not be difficult to read or hardd to find information on card.. lets say easy on eyes yet catchy

```html
<!DOCTYPE html>
<html lang="en">
<head>
<meta charset="utf-8">
<title>Tolvern Security Group – Business Cards</title>
<link rel="stylesheet" href="https://fonts.googleapis.com/css2?family=Tenor+Sans&display=swap">
<style>
  :root {
    --backdrop: #b3b3b1;
    --card: #ffffff;
    --navy: #1f3160;
    --cyan: #0fa3c9;
    --rule: #6d7a98;
  }
  * { margin: 0; padding: 0; box-sizing: border-box; }
  html, body { width: 1200px; height: 848px; overflow: hidden; }
  body {
    background: var(--backdrop);
    font-family: "Tenor Sans", sans-serif;
    color: var(--navy);
    position: relative;
  }
  .card {
    position: absolute;
    background: var(--card);
    border-radius: 14px;
    overflow: hidden;
  }
  .card svg.shapes { position: absolute; inset: 0; }
  .card--front { left: 333px; top: 50px; width: 529px; height: 318px; }
  .card--back  { left: 333px; top: 477px; width: 533px; height: 321px; }

  .brand-name {
    position: absolute;
    font-size: 19px;
    letter-spacing: 0.2px;
    color: var(--navy);
    white-space: nowrap;
  }
  .card--front .brand-name { left: 238px; top: 103px; }
  .card--back .brand-name {
    left: 155px; top: 214px; font-size: 14px;
    transform: translateX(-50%);
  }

  .divider {
    position: absolute;
    left: 262px; top: 46px;
    width: 1px; height: 236px;
    background: var(--rule);
  }
  .contact {
    position: absolute;
    left: 289px; top: 80px;
    list-style: none;
    font-size: 12px;
    line-height: 19.2px;
    color: var(--navy);
  }
</style>
</head>
<body>

<section class="card card--front" aria-label="Card front">
  <svg class="shapes" width="529" height="318" viewBox="0 0 529 318" aria-hidden="true">
    <circle class="brand-dot" cx="127" cy="104" r="48" fill="var(--cyan)"/>
    <circle cx="125" cy="201" r="20" fill="var(--navy)"/>
    <circle cx="217" cy="235" r="29" fill="var(--navy)"/>
    <circle cx="342" cy="268" r="41" fill="var(--navy)"/>
    <circle cx="482" cy="281" r="47" fill="var(--navy)"/>
  </svg>
  <p class="brand-name">TOLVERN SECURITY GROUP</p>
</section>

<section class="card card--back" aria-label="Card back">
  <svg class="shapes" width="533" height="321" viewBox="0 0 533 321" aria-hidden="true">
    <circle cx="-40" cy="-50" r="172" fill="var(--navy)"/>
    <circle cx="590" cy="370" r="175" fill="var(--navy)"/>
    <circle class="brand-dot" cx="151" cy="145" r="38" fill="var(--cyan)"/>
  </svg>
  <p class="brand-name">TOLVERN SECURITY GROUP</p>
  <div class="divider"></div>
  <ul class="contact">
    <li>Mr Daniel Reyes</li>
    <li>Position</li>
    <li>Licence number 1</li>
    <li>License number 2</li>
    <li>www.tolvernsecuritygroup.com.au</li>
    <li>14 harlow street NSW 2600</li>
    <li>dreyes@tolvernsecurity.com.au</li>
    <li>0400 123 456</li>
  </ul>
</section>

</body>
</html>
```